Over The Ridge Mediaworks Business Card
Card design
Over The Ridge Mediaworks Business Card -
Creative Brief
Simple
Simon Ashby
Chief Creative Officer
no address
Simon.Ashby@OverTheRidgeMediaworks.example
OverTheRidgeMediaworks.example
I don't have the source files from my logo project yet but will be uploading soon. Meanwhile please go to: http://entries.markcraftstudio.example/contests/over-the-ridge-logo and refer to winning draft #73 (also draft #5) I would like the front of the card to have the red-background logo plus the web address only
The back of the card will have the black-background logo plus all the personal information in white lettering. I would also like to see a version with the white-background logo and black lettering

```html
<!DOCTYPE html>
<html lang="en">
<head>
<meta charset="utf-8">
<title>Over The Ridge Mediaworks Business Card</title>
<link rel="stylesheet" href="https://fonts.googleapis.com/css2?family=Roboto+Slab:wght@800&family=Open+Sans:wght@400;700&display=swap">
<style>
  :root {
    --red: #d42a2c;
    --black: #121212;
    --white: #ffffff;
    --page: #f3f3f3;
    --grey-text: #444444;
    --shadow: rgba(0, 0, 0, 0.28);
  }
  * { box-sizing: border-box; margin: 0; padding: 0; }
  html, body {
    width: 1200px; height: 607px; overflow: hidden;
    background: var(--page);
    font-family: "Open Sans", Arial, sans-serif;
  }
  .sheet {
    position: relative; width: 1200px; height: 607px;
    display: grid;
    grid-template-columns: repeat(3, 293px);
    grid-template-rows: repeat(2, 180px);
    column-gap: 48px; row-gap: 46px;
    padding: 101px 0 0 112px;
  }
  .card {
    position: relative; border-radius: 12px; overflow: hidden;
    box-shadow: 3px 5px 10px var(--shadow);
    display: flex; flex-direction: column; align-items: center;
  }
  .card--red { background: var(--red); color: var(--white); }
  .card--black { background: var(--black); color: var(--white); }
  .card--white { background: var(--white); color: var(--black); }

  .wordmark {
    font-family: "Roboto Slab", Georgia, serif; font-weight: 800;
    text-align: center; line-height: 1.02; letter-spacing: 0.5px;
    display: flex; align-items: center; gap: 8px;
  }
  .wordmark__dot { width: 10px; height: 10px; border-radius: 50%; flex: none; }
  .card--red .wordmark__dot { background: var(--white); }
  .card--black .wordmark__dot, .card--white .wordmark__dot { background: var(--red); }

  .front .wordmark { margin-top: 22px; font-size: 19px; }
  .front .wordmark__name { display: block; }
  .front .wordmark__sub { display: block; font-size: 12px; letter-spacing: 2px; margin-top: 2px; }

  .contact { margin-top: 16px; text-align: center; font-size: 8px; line-height: 1.35; }
  .contact__name { font-weight: 700; font-size: 9.5px; }
  .contact__title { font-size: 7.5px; margin-bottom: 6px; }
  .card--black .contact__title, .card--white .contact__title { color: var(--red); }
  .contact__label { font-weight: 700; color: var(--red); }
  .card--red .contact__label { color: var(--white); }
  .card--white .contact__line { color: var(--grey-text); }

  .web-band {
    position: absolute; left: 0; right: 0; bottom: 0; height: 20px;
    display: flex; align-items: center; justify-content: center;
    font-size: 7.5px; font-weight: 700; letter-spacing: 1px; color: var(--white);
  }
  .card--red .web-band { background: var(--black); }
  .card--black .web-band, .card--white .web-band { background: var(--red); }

  .back .wordmark { margin-top: 50px; font-size: 22px; }
  .back .web { position: absolute; bottom: 18px; font-size: 7.5px; font-weight: 700; letter-spacing: 1px; }
  .card--white.back .web { color: var(--black); }
</style>
</head>
<body>
<main class="sheet">
  <!-- Front row -->
  <article class="card card--red front">
    <div class="wordmark"><span class="wordmark__dot"></span><span><span class="wordmark__name">OVER THE RIDGE</span><span class="wordmark__sub">MEDIAWORKS</span></span></div>
    <div class="contact">
      <p class="contact__name">Simon Ashby</p>
      <p class="contact__title">Chief Creative Officer</p>
      <p class="contact__line"><span class="contact__label">Cell :</span> 310.555.0147</p>
      <p class="contact__line"><span class="contact__label">Email :</span> Simon.Ashby@OverTheRidgeMediaworks.example</p>
    </div>
    <div class="web-band">www.OverTheRidgeMediaworks.example</div>
  </article>

  <article class="card card--black front">
    <div class="wordmark"><span class="wordmark__dot"></span><span><span class="wordmark__name">OVER THE RIDGE</span><span class="wordmark__sub">MEDIAWORKS</span></span></div>
    <div class="contact">
      <p class="contact__name">Simon Ashby</p>
      <p class="contact__title">Chief Creative Officer</p>
      <p class="contact__line"><span class="contact__label">Cell :</span> 310.555.0147</p>
      <p class="contact__line"><span class="contact__label">Email :</span> Simon.Ashby@OverTheRidgeMediaworks.example</p>
    </div>
    <div class="web-band">www.OverTheRidgeMediaworks.example</div>
  </article>

  <article class="card card--white front">
    <div class="wordmark"><span class="wordmark__dot"></span><span><span class="wordmark__name">OVER THE RIDGE</span><span class="wordmark__sub">MEDIAWORKS</span></span></div>
    <div class="contact">
      <p class="contact__name">Simon Ashby</p>
      <p class="contact__title">Chief Creative Officer</p>
      <p class="contact__line"><span class="contact__label">Cell :</span> 310.555.0147</p>
      <p class="contact__line"><span class="contact__label">Email :</span> Simon.Ashby@OverTheRidgeMediaworks.example</p>
    </div>
    <div class="web-band">www.OverTheRidgeMediaworks.example</div>
  </article>

  <!-- Back row -->
  <article class="card card--red back">
    <div class="wordmark"><span class="wordmark__dot"></span><span>OVER THE<br>RIDGE</span></div>
    <p class="web">www.OverTheRidgeMediaworks.example</p>
  </article>

  <article class="card card--black back">
    <div class="wordmark"><span class="wordmark__dot"></span><span>OVER THE<br>RIDGE</span></div>
    <p class="web">www.OverTheRidgeMediaworks.example</p>
  </article>

  <article class="card card--white back">
    <div class="wordmark"><span class="wordmark__dot"></span><span>OVER THE<br>RIDGE</span></div>
    <p class="web">www.OverTheRidgeMediaworks.example</p>
  </article>
</main>
</body>
</html>
```